Letterhead & Business Card Design Project

Use existing logo to create a new letterhead and business card design. Looking for something clean modern using color options of black, white and gray. The green from the logo may be used lightly as an accent color.

Target Market(s)

Professional business people

Industry/Entity Type

Business

Requirements
Must have
• Business card with front and back design using existing logo.
Nice to have
• Professional presentation
Clean look
Should not have
• No oil rigs, pumpjacks or clip art.

```html
<!DOCTYPE html>
<html lang="en">
<head>
<meta charset="utf-8">
<title>Northfield Survey – Stationery</title>
<link rel="stylesheet" href="https://fonts.googleapis.com/css2?family=Source+Sans+3:wght@400;600&display=swap">
<style>
  :root {
    --backdrop: #c8c5e0;
    --paper: #ffffff;
    --ink: #1a1a1a;
    --ink-soft: #3a3a3a;
    --brand-grey: #4a4a4a;
    --accent: #3db53a;
    --band-grey: #8c8c8c;
    --band-black: #111111;
    --sig-tone: #d9d9d9;
  }
  * { box-sizing: border-box; margin: 0; padding: 0; }
  html, body { width: 1200px; height: 1029px; overflow: hidden; }
  body {
    position: relative;
    background: var(--backdrop);
    font-family: "Source Sans 3", sans-serif;
    color: var(--ink);
  }

  /* ---------- company name ---------- */
  .brand {
    position: absolute;
    font-family: "Source Sans 3", sans-serif;
    font-weight: 400;
    color: var(--brand-grey);
    line-height: 1;
    white-space: nowrap;
    text-align: center;
  }

  /* ---------- letterhead ---------- */
  .letterhead { position: absolute; left: 457px; top: 43px; width: 732px; height: 942px; background: var(--paper); }
  .letterhead .brand { left: 0; width: 100%; top: 52px; font-size: 44px; }

  .letter-body {
    position: absolute; left: 40px; top: 163px; width: 672px;
    font-size: 13.4px; line-height: 17.4px; color: var(--ink);
  }
  .letter-body p { text-align: justify; margin-bottom: 17.4px; }
  .letter-body .salutation, .letter-body .closing { text-align: left; }
  .letter-body .closing { margin-top: 30px; margin-bottom: 0; }

  .signature { position: absolute; left: 17px; top: 722px; width: 150px; height: 86px; background: linear-gradient(120deg, var(--sig-tone), #f2f2f2); border-radius: 4px; }
  .signer { position: absolute; left: 40px; top: 815px; font-size: 13.4px; }

  .letter-footer { position: absolute; left: 0; top: 878px; width: 100%; text-align: center; color: var(--accent); font-size: 12.4px; line-height: 17px; font-weight: 600; }
  .letter-band { position: absolute; left: 0; top: 915px; width: 732px; height: 27px; }

  /* ---------- business cards ---------- */
  .card { position: absolute; width: 299px; height: 172px; background: var(--paper); overflow: hidden; }
  .card-front { left: 91px; top: 385px; }
  .card-back { left: 91px; top: 694px; }

  .card-front .brand { left: 0; width: 100%; top: 30px; font-size: 29px; }

  .holder { position: absolute; left: 0; width: 144px; top: 117px; text-align: right; font-size: 9px; color: var(--accent); font-weight: 600; }
  .card-address { position: absolute; left: 0; width: 144px; top: 134px; text-align: right; font-size: 6.6px; line-height: 8.6px; color: var(--ink); }
  .card-divider { position: absolute; left: 154px; top: 118px; width: 1px; height: 35px; background: var(--ink-soft); }
  .card-contact { position: absolute; left: 162px; top: 122px; font-size: 6.6px; line-height: 9px; color: var(--ink); }
  .card-band { position: absolute; left: 0; top: 155px; width: 299px; height: 17px; }

  .tag { position: absolute; left: 15px; height: 13px; padding: 0 8px 0 12px; background: var(--band-black); color: var(--paper); font-size: 8.4px; line-height: 13px; }
  .tag-expertise { top: 12px; width: 92px; }
  .tag-certified { top: 87px; width: 62px; }
  .skills { position: absolute; left: 19px; list-style: none; font-size: 8.2px; line-height: 11px; }
  .skills li::before { content: "• "; }
  .skills-expertise { top: 28px; }
  .skills-certified { top: 103px; }

  .card-back .brand { left: 194px; top: 67px; width: 150px; font-size: 19px; transform: rotate(-90deg); transform-origin: center; }
</style>
</head>
<body>

  <!-- Letterhead -->
  <section class="letterhead">
    <div class="brand">Northfield Survey</div>

    <div class="letter-body">
      <p class="salutation">Dear,<br>Someone / Somebody</p>
      <p>"Lorem ipsum dolor sit amet, consectetur adipisicing elit, sed do eiusmod tempor incididunt ut labore et dolore magna aliqua. Ut enim ad minim veniam, quis nostrud exercitation ullamco laboris nisi ut aliquip ex ea commodo consequat. Duis aute irure dolor in reprehenderit in voluptate velit esse cillum dolore eu fugiat nulla pariatur. Excepteur sint occaecat cupidatat non proident, sunt in culpa qui officia deserunt mollit anim id est laborum."<br>Section 1.10.32 of "de Finibus Bonorum et Malorum", written by Lucius Avenor in 45 BC</p>
      <p>"Sed ut perspiciatis unde omnis iste natus error sit voluptatem accusantium doloremque laudantium, totam rem aperiam, eaque ipsa quae ab illo inventore veritatis et quasi architecto beatae vitae dicta sunt explicabo. Nemo laboriosam, nisi ut aliquid ex ea commodi consequatur? Quis autem vel eum iure reprehenderit qui in ea voluptate velit esse quam nihil molestiae consequatur, vel illum qui dolorem eum fugiat quo voluptas nulla pariatur?"<br>1914 translation by H. Carlow</p>
      <p>"But I must explain to you how all this mistaken idea of denouncing pleasure and praising pain was born and I will give you a complete account of the system, and expound the actual teachings of the great explorer of the truth, the master-builder of human happiness. No one rejects, dislikes, or avoids pleasure itself, because it is pleasure, but because those who do not know how to pursue pleasure rationally encounter consequences that are extremely painful. Nor again is there anyone who loves or pursues or desires to obtain pain of itself, because it is pain, but because occasionally circumstances occur in which toil and pain can procure him some great pleasure. To take a trivial example, which of us ever undertakes laborious physical exercise, except to obtain some advantage from it? But who has any right to find fault with a man who chooses to enjoy a pleasure that has no annoying consequences, or one who avoids a pain that produces no resultant pleasure?"<br>Section 1.10.33 of "de Finibus Bonorum et Malorum", written by Lucius Avenor in 45 BC</p>
      <p class="closing">Yours Truly,<br>1914 translation by</p>
    </div>

    <div class="signature" role="img" aria-label="Handwritten signature of the sender"></div>
    <div class="signer">H. Carlow</div>

    <div class="letter-footer">
      4420 West Harbor Rd Suite 210 Easton, Kansas 66020<br>
      Phone 555.204.3310 Fax 555.204.3311 www.northfieldsurvey.com
    </div>

    <svg class="letter-band" viewBox="0 0 732 27" preserveAspectRatio="none" aria-hidden="true">
      <rect x="0" y="0" width="732" height="27" fill="var(--band-grey)"/>
      <polygon points="543,0 732,0 732,27 566,27" fill="var(--band-black)"/>
      <polygon points="536,0 543,0 566,27 559,27" fill="var(--paper)"/>
    </svg>
  </section>

  <!-- Business card: front -->
  <section class="card card-front">
    <div class="brand">Northfield Survey</div>

    <div class="holder">Jonah Reyes | President</div>
    <div class="card-address">4420 West Harbor Rd Suite 210 Easton<br>Kansas 66020</div>
    <div class="card-divider"></div>
    <div class="card-contact">
      Phone 555.204.3310<br>
      Fax 555.204.3311<br>
      www.northfieldsurvey.com
    </div>

    <svg class="card-band" viewBox="0 0 299 17" preserveAspectRatio="none" aria-hidden="true">
      <rect x="0" y="0" width="299" height="17" fill="var(--band-grey)"/>
      <polygon points="228,0 299,0 299,17 243,17" fill="var(--band-black)"/>
      <polygon points="224,0 228,0 243,17 239,17" fill="var(--paper)"/>
    </svg>
  </section>

  <!-- Business card: back -->
  <section class="card card-back">
    <div class="tag tag-expertise">EXPERTISE WITH</div>
    <ul class="skills skills-expertise">
      <li>Epoxies</li>
      <li>Urethanes</li>
      <li>Polyureas</li>
      <li>Surface coatings</li>
    </ul>
    <div class="tag tag-certified">CERTIFIED</div>
    <ul class="skills skills-certified">
      <li>Small business</li>
      <li>Hydroseal waterproofing materials</li>
      <li>Confined space</li>
    </ul>

    <div class="brand">Northfield Survey</div>
  </section>

</body>
</html>
```